Computer Problems?

I need a flyer design for our company based on the Sunshine Coast Australia.
Size = A5
We are TV antenna and communication specialists and now have the opportunity to offer PC repair work onsite or in the workshop with over 10 years experience looking after sunshine coast locals
our website is www.brightlinkworks.com
the most important thing for us is that it is eye catching and not too cluttered
We cater for both home and business
NO FIX NO FEE
the services we provide are
tutoring
virus and spyware removal
pc clean up (annual service)
we sell new and second hand computers
hardware and software at very competitive pricing
somehow try to advertise some of the other services we offer.. we can be found on our webpage listed above, however the flyer is all about the computer work.
I have been told that a flyer needs a call to action so I believe 50% off labour on redemption of flyer works.
I am very flexible to the design stuff so go wild.
as a small side note the following design is nice maybe because its clutter free I don't know
http://pixelbidhub.com.au/other-design-tasks/contests/computer-repair-flyer-design-58306
cheers
Tom
Adults, aged 20 and up
home users
business users
Communication

```html
<!DOCTYPE html>
<html lang="en">
<head>
<meta charset="utf-8">
<title>Brightlink Works – Computer Repair Flyer</title>
<link rel="stylesheet" href="https://fonts.googleapis.com/css2?family=Graduate&family=Archivo+Black&family=Arimo:wght@400;700&display=swap">
<style>
  :root {
    --navy: #0d4a9a;
    --deep-blue: #0a52a8;
    --sky-blue: #1f93dc;
    --bright-blue: #2a9be6;
    --yellow: #ffe600;
    --yellow-dark: #f2c200;
    --white: #ffffff;
    --photo-light: #8a9bb0;
    --photo-dark: #2a3340;
  }
  * { margin: 0; padding: 0; box-sizing: border-box; }
  html, body {
    width: 853px; height: 1200px; overflow: hidden;
    background: var(--white);
  }
  .flyer {
    position: absolute; left: 30px; top: 48px;
    width: 800px; height: 1122px; overflow: hidden;
    box-shadow: 0 2px 8px rgba(0,0,0,.35);
    font-family: "Arimo", Arial, sans-serif;
  }
  .flyer-bg, .flyer-swoosh { position: absolute; left: 0; top: 0; width: 800px; height: 1122px; }
  .hero-photo {
    position: absolute; left: 400px; top: 70px; width: 370px; height: 450px;
    background: linear-gradient(160deg, var(--photo-light) 0%, #4a5a6e 45%, var(--photo-dark) 100%);
  }
  .brand {
    position: absolute; left: 32px; top: 70px; width: 384px;
  }
  .brand-name {
    display: flex; align-items: center; gap: 14px;
    font-family: "Archivo Black", sans-serif; font-size: 36px; color: var(--navy);
    letter-spacing: .5px; height: 82px;
  }
  .brand-mark { width: 26px; height: 26px; background: var(--yellow-dark); flex: none; }
  .brand-tagline {
    margin-top: 12px; font-family: "Arimo", sans-serif; font-weight: 700;
    font-size: 16.5px; color: var(--navy); letter-spacing: .3px; white-space: nowrap;
  }
  .headline {
    position: absolute; left: 32px; top: 222px;
    font-family: "Archivo Black", sans-serif; font-size: 28px; line-height: 38px;
    color: var(--navy); letter-spacing: .3px;
  }
  .headline-offer {
    position: absolute; left: 30px; top: 300px;
    font-family: "Graduate", serif; font-size: 46px; color: var(--bright-blue);
    -webkit-text-stroke: 1.5px var(--white);
    text-shadow: 0 2px 0 var(--navy), 0 3px 4px rgba(0,0,0,.35);
    letter-spacing: -1px;
  }
  .section-banner {
    position: absolute; height: 54px; background: var(--yellow);
    font-family: "Graduate", serif; font-size: 30px; color: var(--navy);
    display: flex; align-items: center; padding-left: 12px; white-space: nowrap;
    box-shadow: 0 3px 5px rgba(0,0,0,.25);
  }
  .section-banner::after {
    content: ""; position: absolute; right: 0; bottom: -12px;
    border-top: 12px solid var(--yellow-dark); border-left: 12px solid transparent;
  }
  .banner-services { left: 66px; top: 584px; width: 584px; }
  .banner-other { left: 74px; top: 808px; width: 398px; }
  .mouse-icon { position: absolute; }
  .service-list {
    position: absolute; left: 70px; list-style: none;
    font-size: 15.5px; color: var(--white); line-height: 24px;
    text-shadow: 0 1px 2px rgba(0,0,0,.45);
  }
  .service-list li { padding-left: 23px; position: relative; }
  .service-list li::before {
    content: ""; position: absolute; left: 0; top: 6px; width: 12px; height: 12px;
    border-radius: 50%; background: var(--yellow);
  }
  .list-services { top: 651px; }
  .list-other { top: 876px; }
  .coupon {
    position: absolute; left: 492px; top: 809px; width: 320px; height: 193px;
    border: 2px dashed var(--white); border-right: none; border-radius: 14px 0 0 14px;
  }
  .coupon-figure {
    position: absolute; left: 16px; top: 14px; display: flex; align-items: flex-start;
    color: var(--yellow); font-family: "Graduate", serif;
  }
  .coupon-amount { font-size: 92px; line-height: 100px; letter-spacing: -3px; }
  .coupon-percent { font-family: "Arimo", sans-serif; font-size: 80px; line-height: 100px; margin-left: 4px; }
  .coupon-off {
    font-size: 38px; line-height: 40px; writing-mode: vertical-rl;
    margin-left: 4px; margin-top: 4px;
  }
  .coupon-terms {
    position: absolute; left: 16px; top: 122px; width: 270px;
    color: var(--yellow); font-size: 15.5px; line-height: 25px;
  }
  .call-to-action {
    position: absolute; left: 0; bottom: 0; width: 800px; height: 92px;
    background: linear-gradient(180deg, var(--yellow) 0%, #ffd900 100%);
    display: flex; align-items: center; justify-content: center; text-align: center;
    font-family: "Graduate", serif; font-size: 20.5px; line-height: 25px; color: var(--navy);
  }
</style>
</head>
<body>
<main class="flyer">
  <svg class="flyer-bg" viewBox="0 0 800 1122" aria-hidden="true">
    <defs>
      <linearGradient id="bodyBlue" x1="0" y1="0" x2="0" y2="1">
        <stop offset="0" stop-color="#2b9fe0"/>
        <stop offset=".55" stop-color="#1b7dcc"/>
        <stop offset="1" stop-color="#0c4fa5"/>
      </linearGradient>
    </defs>
    <rect width="800" height="1122" fill="url(#bodyBlue)"/>
    <rect x="520" y="0" width="280" height="540" fill="var(--deep-blue)"/>
    <path d="M0,0 H520 C565,120 560,300 470,370 C380,430 200,445 0,425 Z" fill="var(--white)"/>
    <path d="M500,0 H556 C580,110 575,230 530,300 L505,290 C545,210 545,100 500,0 Z" fill="var(--yellow)"/>
    <path d="M470,0 H500 C545,100 545,210 505,290 L495,284 C530,210 525,100 470,0 Z" fill="#c9ced6"/>
  </svg>

  <div class="hero-photo" role="img" aria-label="Photo of a technician kneeling beside an open desktop computer tower, working on its internals with a screwdriver"></div>

  <svg class="flyer-swoosh" viewBox="0 0 800 1122" aria-hidden="true">
    <path d="M0,420 C220,470 480,520 800,470 L800,505 C480,555 220,500 0,448 Z" fill="var(--yellow)"/>
    <path d="M0,448 C220,500 480,555 800,505 L800,512 C480,562 220,506 0,455 Z" fill="var(--white)"/>
    <path d="M0,455 C220,506 480,562 800,512 L800,530 C480,580 220,520 0,465 Z" fill="var(--yellow)"/>
  </svg>

  <header class="brand">
    <div class="brand-name"><span class="brand-mark"></span>BRIGHTLINK WORKS</div>
    <p class="brand-tagline">DIGITAL TV &amp; COMMUNICATION SPECIALISTS</p>
  </header>

  <h1 class="headline">WE CATER FOR BOTH<br>HOME AND BUSINESS</h1>
  <p class="headline-offer">NO FIX NO FEE</p>

  <svg class="mouse-icon" style="left:18px;top:548px" width="150" height="100" viewBox="0 0 150 100" aria-hidden="true">
    <path d="M40,48 C40,20 90,30 140,14" fill="none" stroke="var(--yellow)" stroke-width="3"/>
    <rect x="22" y="46" width="36" height="52" rx="18" fill="var(--yellow)" stroke="var(--yellow-dark)" stroke-width="2"/>
    <line x1="40" y1="48" x2="40" y2="66" stroke="var(--yellow-dark)" stroke-width="2"/>
  </svg>
  <h2 class="section-banner banner-services">THE SERVICES WE PROVIDE ARE</h2>
  <ul class="service-list list-services">
    <li>TUTORING</li>
    <li>VIRUS AND SPYWARE REMOVAL</li>
    <li>PC CLEAN UP (ANNUAL SERVICE)</li>
    <li>WE SELL NEW AND SECOND HAND COMPUTERS</li>
    <li>HARDWARE AND SOFTWARE AT VERY COMPETITIVE PRICING</li>
  </ul>

  <svg class="mouse-icon" style="left:20px;top:772px" width="150" height="100" viewBox="0 0 150 100" aria-hidden="true">
    <path d="M40,48 C40,20 90,30 140,14" fill="none" stroke="var(--yellow)" stroke-width="3"/>
    <rect x="22" y="46" width="36" height="52" rx="18" fill="var(--yellow)" stroke="var(--yellow-dark)" stroke-width="2"/>
    <line x1="40" y1="48" x2="40" y2="66" stroke="var(--yellow-dark)" stroke-width="2"/>
  </svg>
  <h2 class="section-banner banner-other">OUR OTHER SERVICES</h2>
  <ul class="service-list list-other">
    <li>TELEVISION AMPLIFIERS &amp; BOOSTERS</li>
    <li>INTERCOMS</li>
    <li>HOME AUTOMATION</li>
    <li>TELEPHONE &amp; DATA POINTS</li>
    <li>HOME THEATRE DESIGN &amp; INSTALLATION</li>
  </ul>

  <aside class="coupon">
    <div class="coupon-figure">
      <span class="coupon-amount">50</span><span class="coupon-percent">%</span><span class="coupon-off">OFF</span>
    </div>
    <p class="coupon-terms">LABOUR ON REDEMPTION OF<br>FLYER WORKS</p>
  </aside>

  <footer class="call-to-action">
    <p>CALL BRIGHTLINK WORKS TODAY ON 1300 555 018 FOR ALL<br>YOUR RECEPTION NEEDS</p>
  </footer>
</main>
</body>
</html>
```